Business Card Design

I need a business card and logo for a new company based in Manhattan, Kansas called "Ferncliff Works, LLC". I am a project management consultant. I specialize in laying the foundation for businesses and business owners to get their projects on track. Think of it as if you were wanting to go from coast to coast on a train. Before you can jump on the train and sell tickets, you have to design the path the train will take, acquire the land, clear the trees, level the ground, prepare the base for the track, lay the track and finally place the train on the track (That's what I do with my clients). Once the train is on the track and I've provided them with the operations manual, then they and their managers get to drive the train. I don't have color preferences. The final design should communicate a clear direction or path to growing the customer's business.
Updates

Since I am in need of a logo as well, I have also created a logo design project that will work in conjunction with this project.

Reason: Accepted a company logo this afternoon that I would like to have cards designed around. Sorry for jumping the gun and posting both projects at the same time.

Industry/Entity Type

Business

Contact Information for Business Card

Owner: Dale Purvis. Business Name: Ferncliff Works, LLC. Business Address: 4871 Marlow Bend, Manhattan, KS, 66921. Business Phone Number: 785-640-1572. Business Email: dale@ferncliffworksllc.example

```html
<!DOCTYPE html>
<html lang="en">
<head>
<meta charset="utf-8">
<title>Ferncliff Works, LLC – Business Card</title>
<link rel="stylesheet" href="https://fonts.googleapis.com/css2?family=Encode+Sans+Condensed:wght@300;400&family=Jura:wght@400&display=swap">
<style>
  :root {
    --page-bg: #ffffff;
    --card-bg: #e6e6e7;
    --card-edge: #4a4a4a;
    --band-dark: #a7a8aa;
    --band-light: #b9bbbe;
    --band-sand: #e2dccb;
    --header-text: #f4f4f4;
    --body-text: #a1a2a4;
  }
  html, body {
    margin: 0;
    padding: 0;
    width: 1200px;
    height: 1000px;
    overflow: hidden;
    background: var(--page-bg);
  }
  .canvas {
    position: relative;
    width: 1200px;
    height: 1000px;
  }
  .business-card {
    position: absolute;
    left: 178px;
    top: 157px;
    width: 447px;
    height: 720px;
    background: var(--card-bg);
    outline: 1px solid var(--card-edge);
    overflow: hidden;
  }
  .chevron-bands {
    position: absolute;
    left: 0;
    top: 0;
    width: 447px;
    height: 720px;
  }
  .band-sand { fill: var(--band-sand); }
  .band-light { fill: var(--band-light); }
  .band-dark { fill: var(--band-dark); }

  .company-name {
    position: absolute;
    left: 0;
    top: 38px;
    width: 100%;
    margin: 0;
    text-align: center;
    font-family: "Encode Sans Condensed", sans-serif;
    font-weight: 300;
    font-size: 44px;
    letter-spacing: 0.5px;
    color: var(--header-text);
  }
  .brand-mark {
    position: absolute;
    left: 0;
    top: 150px;
    width: 100%;
    display: flex;
    justify-content: center;
    align-items: center;
    gap: 10px;
    font-family: "Encode Sans Condensed", sans-serif;
    font-weight: 300;
    font-size: 30px;
    color: var(--header-text);
  }
  .brand-mark .brand-square {
    width: 18px;
    height: 18px;
    background: var(--header-text);
  }
  .person-name {
    position: absolute;
    left: 0;
    top: 384px;
    width: 100%;
    margin: 0;
    text-align: center;
    font-family: "Jura", sans-serif;
    font-weight: 400;
    font-size: 62px;
    letter-spacing: 2px;
    color: var(--body-text);
  }
  .contact-list {
    position: absolute;
    left: 10px;
    top: 524px;
    margin: 0;
    padding: 0;
    list-style: none;
    font-family: "Encode Sans Condensed", sans-serif;
    font-weight: 400;
    font-size: 28px;
    line-height: 37px;
    color: var(--body-text);
  }
  .contact-item {
    display: flex;
    align-items: flex-start;
    margin-bottom: 12px;
  }
  .contact-icon {
    flex: none;
    width: 42px;
    height: 37px;
    margin-right: 16px;
    fill: var(--body-text);
    stroke: var(--body-text);
  }
  .contact-item.address .contact-icon { margin-right: 23px; }
</style>
</head>
<body>
<div class="canvas">
  <section class="business-card" aria-label="Business card for Ferncliff Works, LLC">
    <svg class="chevron-bands" viewBox="0 0 447 720" aria-hidden="true">
      <polygon class="band-sand" points="0,0 447,0 447,203 224,366 0,203"/>
      <polygon class="band-light" points="0,0 447,0 447,178 224,341 0,178"/>
      <polygon class="band-dark" points="0,0 447,0 447,153 224,318 0,153"/>
    </svg>

    <h1 class="company-name">Ferncliff Works, LLC</h1>
    <div class="brand-mark"><span class="brand-square"></span><span>Ferncliff Works</span></div>

    <h2 class="person-name">Dale Purvis</h2>

    <ul class="contact-list">
      <li class="contact-item address">
        <svg class="contact-icon" viewBox="0 0 42 37" aria-hidden="true">
          <polygon points="21,3 2,19 7,19 7,34 17,34 17,24 25,24 25,34 35,34 35,19 40,19" stroke="none"/>
        </svg>
        <span>4871 Marlow Bend,<br>Manhattan, KS, 66921</span>
      </li>
      <li class="contact-item phone">
        <svg class="contact-icon" viewBox="0 0 42 37" aria-hidden="true">
          <circle cx="19" cy="19" r="16" fill="none" stroke-width="1.5"/>
          <path d="M14 10 q-4 9 5 18 l4 -3 l-3 -4 l-2 1 q-3 -4 -1 -8 l2 0 l0 -5 z" stroke="none"/>
        </svg>
        <span>785-640-1572</span>
      </li>
      <li class="contact-item email">
        <svg class="contact-icon" viewBox="0 0 42 37" aria-hidden="true">
          <rect x="3" y="9" width="34" height="21" fill="none" stroke-width="1.5"/>
          <polyline points="3,9 20,21 37,9" fill="none" stroke-width="1.5"/>
          <polyline points="3,30 16,18 M24,18 37,30" fill="none" stroke-width="1.5"/>
        </svg>
        <span>dale@ferncliffworksllc.example</span>
      </li>
    </ul>
  </section>
</div>
</body>
</html>
```